Business card alterations

I have changed my business name from Brisa Laser Renewal Clinic to simply "Brisa Laser Clinic' and need this logo changed to reflect same

Brisa Laser Clinic
Est. 2004

I also need new business cards with above logo included and this attached card changed to the following.
Marcia Pellbrook
Dermal Aesthetician
Grad Cert in Laser & IPL Treatments

I need at least one logo in less than 4mb so I can upload into my newsletter format so I can upload to newsletters, emails etc

Thanks
Marcie

```html
<!DOCTYPE html>
<html lang="en">
<head>
<meta charset="utf-8">
<title>Brisa Laser Clinic – Business Cards</title>
<link rel="stylesheet" href="https://fonts.googleapis.com/css2?family=Arimo:wght@400;700&family=PT+Sans:wght@400;700&display=swap">
<style>
  :root {
    --page-bg: #ffffff;
    --card-green: #27d627;
    --card-ink: #ffffff;
    --rule: rgba(255, 255, 255, 0.85);
  }
  * { margin: 0; padding: 0; box-sizing: border-box; }
  html, body {
    width: 1200px;
    height: 848px;
    overflow: hidden;
    background: var(--page-bg);
  }
  .sheet {
    position: relative;
    width: 1200px;
    height: 848px;
  }
  .business-card {
    position: absolute;
    width: 471px;
    height: 297px;
    background: var(--card-green);
    color: var(--card-ink);
    font-family: "Arimo", Arial, sans-serif;
  }
  .card-top-left { left: 86px; top: 107px; }
  .card-top-right { left: 605px; top: 107px; }
  .card-bottom-left { left: 86px; top: 434px; }
  .card-bottom-right { left: 605px; top: 434px; }

  .brand-name {
    position: absolute;
    left: 0;
    width: 463px;
    top: 22px;
    text-align: center;
    font-family: "Arimo", Arial, sans-serif;
    font-weight: 400;
    font-size: 86px;
    line-height: 100px;
    letter-spacing: -1px;
  }
  .brand-tagline,
  .brand-established {
    position: absolute;
    left: 0;
    width: 463px;
    text-align: center;
    font-size: 11px;
    line-height: 13px;
    letter-spacing: 0.62em;
    text-indent: 0.62em;
  }
  .brand-tagline { top: 141px; }
  .brand-established { top: 156px; letter-spacing: 0.5em; text-indent: 0.5em; }

  .holder {
    position: absolute;
    top: 177px;
    text-align: right;
  }
  .holder-name {
    font-weight: 700;
    font-size: 15px;
    line-height: 20px;
    letter-spacing: -0.3px;
  }
  .holder-role {
    font-size: 12px;
    line-height: 20px;
  }
  .holder-title {
    font-family: "PT Sans", Arial, sans-serif;
    font-weight: 700;
    font-size: 16px;
    line-height: 23px;
  }
  .holder-left-aligned { text-align: left; }

  .divider {
    position: absolute;
    top: 180px;
    width: 1px;
    height: 83px;
    background: var(--rule);
  }

  .contact-list {
    position: absolute;
    top: 179px;
    list-style: none;
    font-size: 12px;
    line-height: 18px;
    letter-spacing: -0.2px;
  }
  .contact-phone { font-weight: 700; }
</style>
</head>
<body>
<main class="sheet">

  <article class="business-card card-top-left">
    <div class="brand-name">Brisa</div>
    <div class="brand-tagline">LASER CLINIC</div>
    <div class="brand-established">EST. 2004</div>
    <div class="holder" style="right:249px;">
      <p class="holder-name">Marcie Pellbrook</p>
    </div>
    <span class="divider" style="left:236px;"></span>
    <ul class="contact-list" style="left:250px;">
      <li class="contact-phone">T (08) 7412 3390</li>
      <li>info@brisa.com.au</li>
      <li>www.brisa.com.au</li>
      <li>214 Ashcombe Road</li>
      <li>Kenwick SA 5071</li>
    </ul>
  </article>

  <article class="business-card card-top-right">
    <div class="brand-name">Brisa</div>
    <div class="brand-tagline">LASER CLINIC</div>
    <div class="brand-established">EST. 2004</div>
    <div class="holder" style="right:248px;">
      <p class="holder-name">Rosalind Hartley</p>
      <p class="holder-role">Clinic Manager</p>
    </div>
    <span class="divider" style="left:237px;"></span>
    <ul class="contact-list" style="left:251px;">
      <li class="contact-phone">T (08) 7412 3390</li>
      <li>info@brisa.com.au</li>
      <li>www.brisa.com.au</li>
      <li>214 Ashcombe Road</li>
      <li>Kenwick SA 5071</li>
    </ul>
  </article>

  <article class="business-card card-bottom-left">
    <div class="brand-name">Brisa</div>
    <div class="brand-tagline">LASER CLINIC</div>
    <div class="brand-established">EST. 2004</div>
    <div class="holder" style="right:232px; top:175px;">
      <p class="holder-title">Dermal Aesthetician</p>
    </div>
    <span class="divider" style="left:248px;"></span>
    <ul class="contact-list" style="left:262px;">
      <li class="contact-phone">T (08) 7412 3390</li>
      <li>info@brisa.com.au</li>
      <li>www.brisa.com.au</li>
      <li>214 Ashcombe Road</li>
      <li>Kenwick SA 5071</li>
    </ul>
  </article>

  <article class="business-card card-bottom-right">
    <div class="brand-name">Brisa</div>
    <div class="brand-tagline">LASER CLINIC</div>
    <div class="brand-established">EST. 2004</div>
    <div class="holder holder-left-aligned" style="left:80px; top:175px;">
      <p class="holder-title">Grad Cert in Laser &amp;<br>IPL Treatments</p>
    </div>
    <span class="divider" style="left:247px;"></span>
    <ul class="contact-list" style="left:261px;">
      <li class="contact-phone">T (08) 7412 3390</li>
      <li>info@brisa.com.au</li>
      <li>www.brisa.com.au</li>
      <li>214 Ashcombe Road</li>
      <li>Kenwick SA 5071</li>
    </ul>
  </article>

</main>
</body>
</html>
```